Surviving Domestic Violence Flyer

I need a flyer that "POPS" to attract participants for my research project. I have added the important information on my draft flyer.

```html
<!DOCTYPE html>
<html lang="en">
<head>
<meta charset="utf-8">
<title>Request for Study Participants – Perceived Effectiveness of Domestic Violence Services</title>
<link rel="stylesheet" href="https://fonts.googleapis.com/css2?family=Quicksand:wght@500;700&family=Roboto+Condensed:wght@400;500&display=swap">
<style>
  :root {
    --plum: #5e1a4b;
    --plum-dark: #3a1530;
    --coral: #ec5a3c;
    --band-light: #efe9ee;
    --ink: #1d1d1d;
    --grey-ink: #333;
    --white: #ffffff;
  }
  * { margin: 0; padding: 0; box-sizing: border-box; }
  html, body { width: 928px; height: 1200px; overflow: hidden; background: var(--white); }
  .flyer { position: relative; width: 928px; height: 1200px; overflow: hidden; background: var(--white); }

  .mosaic { position: absolute; left: 0; top: 0; width: 928px; height: 1200px; pointer-events: none; }

  .request-band {
    position: absolute; left: 0; top: 0; width: 605px; height: 78px;
    background: var(--band-light);
    clip-path: polygon(0 0, 100% 0, 93% 100%, 0 100%);
  }
  .request-line {
    position: absolute; left: 48px; top: 22px;
    font-family: "Quicksand", sans-serif; font-weight: 500; font-size: 28px; color: var(--coral);
  }
  .request-line strong { font-weight: 700; font-size: 34px; color: var(--plum); }

  .title {
    position: absolute; left: 48px; top: 104px;
    font-family: "Roboto Condensed", sans-serif; font-weight: 500; font-size: 52px; line-height: 61px;
    color: var(--plum);
  }
  .title .accent { color: var(--coral); }

  .criteria { position: absolute; left: 0; top: 283px; list-style: none; }
  .criteria li {
    position: relative; padding-left: 44px;
    font-family: "Quicksand", sans-serif; font-weight: 500; font-size: 21px; line-height: 29px; color: var(--ink);
  }
  .criteria li::before {
    content: ""; position: absolute; left: 0; top: 6px;
    border-left: 20px solid var(--coral); border-top: 9px solid transparent; border-bottom: 9px solid transparent;
  }
  .criteria li.alt::before { border-left-color: var(--plum); }
  .criteria li + li { margin-top: 25px; }

  .eligibility {
    position: absolute; left: 28px; top: 712px; width: 570px; height: 104px;
    background: var(--white); box-shadow: 1px 3px 6px rgba(0,0,0,.35);
    display: flex; align-items: center; justify-content: center; text-align: center;
    font-family: "Roboto Condensed", sans-serif; font-size: 19px; line-height: 25px; color: var(--grey-ink);
    padding: 0 14px;
  }

  .compensation {
    position: absolute; left: 118px; top: 850px;
    font-family: "Quicksand", sans-serif; font-weight: 700; font-size: 26px; color: var(--plum);
  }

  .footer-scene {
    position: absolute; left: 0; top: 903px; width: 928px; height: 297px;
    background: linear-gradient(180deg, #4a2440 0%, #3b1d36 35%, #2b1528 75%, #1c0f1a 100%);
  }
  .contact-tab {
    position: absolute; left: 0; top: 903px; width: 430px; height: 62px;
    background: var(--plum-dark);
    clip-path: polygon(0 0, 86% 0, 100% 100%, 0 100%);
  }
  .contact-tab span {
    position: absolute; left: 42px; top: 16px;
    font-family: "Roboto Condensed", sans-serif; font-size: 24px; color: var(--coral);
  }

  .contact { position: absolute; font-family: "Roboto Condensed", sans-serif; color: var(--white); font-size: 22px; line-height: 31px; }
  .contact-address { left: 45px; top: 992px; }
  .contact-name { font-size: 30px; line-height: 40px; color: var(--coral); }
  .contact-lines { left: 455px; top: 1027px; }
  .contact-lines .label-value { color: var(--coral); }
</style>
</head>
<body>
<main class="flyer">
  <div class="footer-scene" role="img" aria-label="Dusky purple stormy sky over a flat horizon"></div>

  <svg class="mosaic" viewBox="0 0 928 1200" role="img" aria-label="Mosaic of pink, coral and maroon triangles framing a black-and-white photo of a woman's eye">
    <defs>
      <linearGradient id="mosaic-tone" x1="0" y1="0" x2="1" y2="1">
        <stop offset="0" stop-color="#e0503a"/>
        <stop offset="0.35" stop-color="#b8335d"/>
        <stop offset="0.6" stop-color="#7a1e3c"/>
        <stop offset="1" stop-color="#d2455a"/>
      </linearGradient>
    </defs>
    <polygon fill="url(#mosaic-tone)" points="720,0 928,0 928,965 725,965 790,830 655,830 517,690 517,550 650,550 585,410 585,275 655,140"/>
  </svg>

  <div class="request-band"></div>
  <p class="request-line">Request for <strong>Study Participants</strong></p>

  <h1 class="title">Perceived Effectiveness of<br><span class="accent">Domestic Violence</span> Services</h1>

  <ul class="criteria">
    <li>Are you eighteen years of age or older?</li>
    <li class="alt">Have you been a victim of domestic violence?</li>
    <li>Have you sought assistance with abuse<br>in the last 12 months?</li>
    <li class="alt">Are you still in contact with the person<br>who abused you?</li>
    <li>Are you willing and open to discussing<br>your experience with abuse and your<br>attempts to access services or resources?</li>
  </ul>

  <p class="eligibility">If you answered yes to all of these questions, you may be eligible to participate in a study to better understand the resources needed and services expected for survivors of domestic violence</p>

  <p class="compensation">Participants will be compensated for their time</p>

  <div class="contact-tab"><span>Contact &amp; additional information</span></div>

  <address class="contact contact-address">
    <div class="contact-name">Dana Whitfield</div>
    Lakeshore Metropolitan University<br>
    Dept. of Criminology, Law and Justice<br>
    PO Box 315820<br>
    60612 Chicago, IL
  </address>

  <div class="contact contact-lines">
    Phone: <span class="label-value">1(555)014-2368</span><br>
    Email: <span class="label-value">survivorvoices.study@example.org</span>
  </div>
</main>
</body>
</html>
```